Business Card and Letterhead for Vantage Psychology

We need a business card design and letterhead to use for our Psychology firm that specializes in psychoeducational assessments and individual therapy. Our motto is Purpose-Driven Assessments, Meaning-Centered Therapy.Our contact information is as follows:
Vantage Psychology
The Marwick Block - 6127-48St.
Box 2716 Olds, AB
T2K 3M8
t 403.555.0148 (VANT)
f 403.555.0172
www.vantagepsychology-example.ca
The business card will be used for two different psychologists so I can supply names nearer to completion. We prefer clean, uncluttered looks.

Target Market(s)

Clients, Educators

Font styles to use
Sans Serif

Colors

Designer to choose colors to be used in the design.

Requirements
Must have
• All relevant contact info, logo, some "white" space.
Nice to have
• It would be nice to see letterhead options that have the logo on the top of the page but also options that have it on the side. I think top of the page is probably our preference.
Should not have
• Too much clutter!

```html
<!DOCTYPE html>
<html lang="en">
<head>
<meta charset="utf-8">
<title>Vantage Psychology – Letterhead and Business Cards</title>
<link rel="stylesheet" href="https://fonts.googleapis.com/css2?family=Source+Sans+3:wght@400;600;700&display=swap">
<style>
  :root {
    --bg: #e4e5e7;
    --paper: #ffffff;
    --sky: #5bbfdc;
    --sky-deep: #00b3da;
    --orange: #f4aa55;
    --orange-deep: #f5973a;
    --ink: #6b6b6b;
    --pill: #333333;
  }
  * { box-sizing: border-box; margin: 0; padding: 0; }
  html, body { width: 1200px; height: 1200px; overflow: hidden; }
  body {
    position: relative;
    background: var(--bg);
    font-family: "Source Sans 3", sans-serif;
  }

  /* Letterhead */
  .letterhead {
    position: absolute; left: 175px; top: 143px;
    width: 662px; height: 936px;
    background: var(--paper);
  }
  .letterhead-mark {
    position: absolute; left: 303px; top: 37px;
    width: 56px; height: 56px; border-radius: 50%;
    background: var(--sky);
  }
  .letterhead-rule {
    position: absolute; left: 0; right: 0; top: 92px;
    display: flex; align-items: center; gap: 10px;
  }
  .rule { flex: 1; height: 4px; }
  .rule-sky { background: var(--sky); }
  .rule-orange { background: var(--orange); }
  .brand-name {
    color: var(--sky);
    font-weight: 600;
    text-transform: uppercase;
    letter-spacing: 0.06em;
    white-space: nowrap;
  }
  .letterhead-rule .brand-name { font-size: 16px; }

  .letterhead-footer {
    position: absolute; left: 0; right: 0; bottom: 0; height: 45px;
    background: var(--orange);
    z-index: 1;
  }
  .footer-band {
    position: absolute; left: 0; top: 0; width: 370px; height: 45px;
    background: var(--sky);
    clip-path: polygon(0 0, 100% 0, 94.3% 100%, 0 100%);
  }
  .footer-item {
    position: absolute; top: 10px;
    display: flex; align-items: center; gap: 6px;
    color: #fff; font-size: 9px; line-height: 12px;
  }
  .footer-item svg { width: 11px; height: 14px; fill: #fff; }
  .footer-divider { width: 1px; height: 27px; background: #fff; }
  .footer-address { left: 46px; }
  .footer-phone { left: 216px; }
  .web-pill {
    position: absolute; right: 40px; bottom: 35px;
    z-index: 2;
    background: var(--pill); color: #fff;
    font-size: 9.5px; font-weight: 700; line-height: 13px;
    padding: 5px 11px; border-radius: 4px;
    white-space: nowrap;
  }

  /* Business cards */
  .card {
    position: absolute; left: 694px; width: 396px; height: 240px;
    background: var(--sky-deep);
  }
  .card-front { top: 394px; }
  .card-front .card-base {
    position: absolute; left: 0; right: 0; bottom: 0; height: 23px;
    background: var(--orange-deep);
  }
  .card-front .card-face {
    position: absolute; left: 15px; top: 15px; width: 366px; height: 209px;
    background: var(--paper);
    display: flex; flex-direction: column; align-items: center; justify-content: center; gap: 14px;
    padding-top: 16px;
  }
  .card-mark { width: 74px; height: 74px; border-radius: 50%; background: var(--sky); }
  .card-front .brand-name { font-size: 23px; }

  .card-back { top: 661px; }
  .card-back .card-face {
    position: absolute; left: 5px; top: 7px; width: 386px; height: 198px;
    background: var(--paper);
  }
  .card-back .brand-name {
    position: absolute; left: 0; right: 0; top: 84px;
    text-align: center; font-size: 19px; line-height: 24px;
  }
  .card-contact {
    position: absolute; top: 121px; left: 0; right: 0;
    display: flex; justify-content: center; gap: 10px;
    color: var(--ink); font-size: 12px; line-height: 16.5px;
  }
  .card-address { text-align: right; }
  .card-divider { width: 1px; height: 58px; background: #aaa; }
  .card-phones { padding-top: 7px; }
  .card-web {
    position: absolute; left: 0; right: 0; bottom: 0; height: 35px;
    display: flex; align-items: center; justify-content: center;
    color: #fff; font-size: 11.5px; font-weight: 700;
  }
</style>
</head>
<body>

<section class="letterhead" aria-label="Letterhead">
  <div class="letterhead-mark"></div>
  <div class="letterhead-rule">
    <span class="rule rule-sky"></span>
    <span class="brand-name">Vantage Psychology</span>
    <span class="rule rule-orange"></span>
  </div>

  <footer class="letterhead-footer">
    <div class="footer-band"></div>
    <div class="footer-item footer-address">
      <svg viewBox="0 0 12 16" aria-hidden="true"><path d="M6 0a6 6 0 0 0-6 6c0 4.5 6 10 6 10s6-5.5 6-10a6 6 0 0 0-6-6zm0 8.3A2.3 2.3 0 1 1 6 3.7a2.3 2.3 0 0 1 0 4.6z"/></svg>
      <span class="footer-divider"></span>
      <span>The Marwick Block - 6127-48St.<br>Box 2716 Olds, AB,&nbsp; T2K 3M8</span>
    </div>
    <div class="footer-item footer-phone">
      <svg viewBox="0 0 12 16" aria-hidden="true"><path d="M3 0l2.5 3.5-1.6 1.4c.3 2.3 1.2 4.6 2.8 6.4l1.9-.8L11 14l-2 1.8C3.5 15 .2 7.5 1 1.5z"/></svg>
      <span class="footer-divider"></span>
      <span>T:&nbsp; 403.555.0148 (VANT)<br>F:&nbsp; 403.555.0172</span>
    </div>
  </footer>
  <div class="web-pill">www.vantagepsychology-example.ca</div>
</section>

<section class="card card-front" aria-label="Business card front">
  <div class="card-base"></div>
  <div class="card-face">
    <div class="card-mark"></div>
    <span class="brand-name">Vantage Psychology</span>
  </div>
</section>

<section class="card card-back" aria-label="Business card back">
  <div class="card-face">
    <div class="brand-name">Vantage Psychology</div>
    <div class="card-contact">
      <div class="card-address">The Marwick Block - 6127-48St.<br>Box 2716 Olds, AB<br>T2K 3M8</div>
      <span class="card-divider"></span>
      <div class="card-phones">T:&nbsp; 403.555.0148 (VANT)<br>F:&nbsp; 403.555.0172</div>
    </div>
  </div>
  <div class="card-web">www.vantagepsychology-example.ca</div>
</section>

</body>
</html>
```